Provide bookkeeping and accounting services to small and growing businesses

We need website and logo design using the name Dunhaven as the logo.
The target audience are small companies and startups who need:
1) Simple bookkeeping services
2) Accounting advice that only someone with many years of senior financial experience as a CPA can provide.

The services are provided by two individuals. each of whom specialize in one of the areas.

We want the website to be clean without a lot of visual distraction but don't know how to make a boring subject interesting. We believe our potential clients, small business owners, need to find what they want quickly and easily without a lot of verbiage or distractions.

We've attached a draft of the homepage and have completed the text on most of the other pages.

Target Market(s)

small and early stage growth companies in San Diego North County

Industry/Entity Type

Accounting

Number of Pages Required

1 page

Font styles to use
Sans Serif

Colors
86cfc6
33b8a4
85cae6

Requirements
Must have
• We need a design for the website homepage that includes the name Dunhaven as the logo. Must include a design for the name.
• Must have color in teal or greenish blue.
Nice to have
• White background, clean, clear, uncluttered.
• We would like to use the design in a Theme on a WordPress website. Themes Quiet Meadow and Silver Orchard are appealing to us.
Should not have
• Moving pictures

```html
<!DOCTYPE html>
<html lang="en">
<head>
<meta charset="utf-8">
<title>Dunhaven — Accounting and Bookkeeping</title>
<link rel="stylesheet" href="https://fonts.googleapis.com/css2?family=Cinzel:wght@400;500&family=Open+Sans:wght@300;400;600&display=swap">
<style>
:root{
  --teal:#33b8a4;
  --teal-soft:#86cfc6;
  --sky:#85cae6;
  --ink:#333;
  --muted:#777;
  --light-bg:#f3f3f3;
  --dark:#2e2e2e;
  --darker:#222;
  --white:#fff;
}
*{box-sizing:border-box;margin:0;padding:0}
html,body{width:1200px;height:2913px;overflow:hidden}
body{font-family:"Open Sans",Arial,sans-serif;color:var(--ink);background:var(--white);position:relative}
.abs{position:absolute}
.heading{font-family:"Cinzel",Georgia,serif;font-weight:400;text-align:center}

/* header */
.site-header{top:0;left:0;width:1200px;height:101px;border-top:4px solid var(--teal);background:var(--white)}
.brand{left:97px;top:20px;color:var(--teal)}
.brand-name{font-family:"Cinzel",Georgia,serif;font-size:34px;letter-spacing:2px;line-height:40px}
.brand-tag{font-family:"Cinzel",Georgia,serif;font-size:9.5px;letter-spacing:1.6px;margin-top:2px}
.main-nav a{position:absolute;top:42px;font-size:14px;color:#555;text-decoration:none}
.main-nav a.active{color:var(--teal)}

/* hero */
.hero{top:101px;left:0;width:1200px;height:515px;background:linear-gradient(120deg,#4b4a49 0%,#6e6b66 35%,#a8a49e 60%,#5b5853 100%)}
.hero-caption{left:134px;top:175px;width:612px;height:175px;background:rgba(51,184,164,.85);padding:22px 34px;color:var(--white)}
.hero-caption h1{font-weight:300;font-size:46px;letter-spacing:2px;line-height:52px}
.hero-caption p{font-weight:300;font-size:23px;line-height:31px;margin-top:8px}
.hero-arrow{top:242px;width:34px;height:34px}

/* welcome */
.welcome-title{top:664px;left:0;width:1200px;font-size:30px;color:#444}
.welcome-sub{top:703px;left:0;width:1200px;font-size:23px;color:var(--teal)}
.welcome-text{top:744px;left:230px;width:740px;font-size:12px;line-height:21px;color:#666;text-align:center}
.feature{top:823px;width:307px;text-align:center}
.feature-img{width:307px;height:191px}
.feature h3{margin-top:28px;font-size:16px;font-weight:400;color:#333;letter-spacing:.5px;line-height:22px}
.feature h3.hl{color:var(--teal)}
.feature p{margin-top:8px;font-size:11.5px;line-height:21px;color:#666;white-space:nowrap}
.feature-line{top:1150px;width:307px;height:3px;background:var(--teal-soft)}

/* services */
.services{top:1214px;left:0;width:1200px;height:402px;background:var(--light-bg)}
.services-title{top:1266px;left:0;width:1200px;font-size:32px;color:#444}
.service{width:307px}
.service svg{position:absolute;left:0;top:2px}
.service h4{margin-left:48px;font-size:19px;font-weight:400;color:#444}
.service p{margin-left:48px;margin-top:6px;font-size:12px;line-height:21px;color:#777;text-align:justify}

/* stats */
.stats{top:1616px;left:0;width:1200px;height:415px;background:linear-gradient(135deg,#3bb5a4 0%,#33a99a 55%,#2e9c8f 100%)}
.stats-title{top:1666px;left:0;width:1200px;font-size:34px;color:var(--white)}
.stats-text{top:1718px;left:170px;width:860px;font-size:14px;line-height:27px;color:var(--white);text-align:center}
.stat{top:1798px;width:160px;height:160px;color:var(--white);text-align:center}
.stat svg{position:absolute;left:0;top:0}
.stat b{position:absolute;left:0;top:54px;width:160px;font-size:25px;font-weight:600}
.stat span{position:absolute;left:0;top:92px;width:160px;font-size:11px;text-transform:uppercase}

/* testimonials */
.testi-title{top:2080px;left:0;width:1200px;font-size:32px;color:#444}
.quote-card{top:2183px;width:322px;height:128px;background:#f7f7f7;border:1px solid #ececec;padding:40px 14px 0 16px;font-size:11px;line-height:18px;color:#888;white-space:nowrap;overflow:hidden}
.quote-pin{top:2154px;width:58px;height:58px}
.author{top:2327px}
.avatar{width:62px;height:62px;border-radius:50%;border:3px solid var(--teal-soft);background:linear-gradient(160deg,#c9b9a8,#8c7a6b)}
.author-name{top:2336px;font-size:16px;color:#444}
.author-role{top:2363px;font-size:12px;color:#666}

/* newsletter + footer */
.newsletter{top:2453px;left:0;width:1200px;height:392px;background:var(--dark)}
.news-title{top:2490px;left:0;width:1200px;font-size:24px;color:var(--white);letter-spacing:1px}
.news-sub{top:2526px;left:0;width:1200px;font-size:16px;color:#ccc;text-align:center}
.news-input{top:2575px;left:350px;width:388px;height:43px;background:#3b3b3b;color:#888;font-size:11px;padding:14px 20px}
.news-btn{top:2575px;left:738px;width:70px;height:43px;background:var(--teal)}
.foot-col{top:2683px}
.foot-col h5{font-family:"Cinzel",Georgia,serif;font-weight:400;font-size:18px;color:var(--white);letter-spacing:.5px}
.foot-col a{display:block;font-size:11px;color:#bbb;text-decoration:none;line-height:24px}
.foot-col h5+a{margin-top:8px}
.bottom-bar{top:2845px;left:0;width:1200px;height:68px;background:var(--darker);color:#777;font-size:12px;text-align:center;line-height:68px}
</style>
</head>
<body>

<header class="site-header abs">
  <div class="brand abs">
    <div class="brand-name">DUNHAVEN</div>
    <div class="brand-tag">ACCOUNTING AND BOOKKEEPING</div>
  </div>
  <nav class="main-nav">
    <a class="active" style="left:498px">Home</a>
    <a style="left:587px">About Us</a>
    <a style="left:695px">Services</a>
    <a style="left:797px">Experience</a>
    <a style="left:918px">Resources</a>
    <a style="left:1033px">Contact Us</a>
  </nav>
</header>

<section class="hero abs" role="img" aria-label="Photo of business people reviewing financial documents at a desk">
  <div class="hero-caption abs">
    <h1>DUNHAVEN</h1>
    <p>We simple book keeping services, financial<br>&amp; accounting advice for small start up companies.</p>
  </div>
  <svg class="hero-arrow abs" style="left:33px" viewBox="0 0 34 34"><circle cx="17" cy="17" r="15" fill="none" stroke="#ddd" stroke-width="1.5"/><path d="M20 10l-7 7 7 7" fill="none" stroke="#ddd" stroke-width="2"/></svg>
  <svg class="hero-arrow abs" style="left:1133px" viewBox="0 0 34 34"><circle cx="17" cy="17" r="15" fill="none" stroke="#ddd" stroke-width="1.5"/><path d="M14 10l7 7-7 7" fill="none" stroke="#ddd" stroke-width="2"/></svg>
</section>

<h2 class="welcome-title heading abs">Welcome To Dunhaven</h2>
<p class="welcome-sub heading abs">We are Accounting and Bookkeeping</p>
<p class="welcome-text abs">Dunhaven offers a flexible range of accounting and bookkeeping services and support for small and growing organizations in San Diego North County. We provide bookkeeping services specializing in LedgerWise® at your offices or remotely from ours.</p>

<article class="feature abs" style="left:99px">
  <div class="feature-img" role="img" aria-label="Photo of a pink piggy bank on banknotes" style="background:linear-gradient(160deg,#f4f2ef,#d9c7c4 50%,#b9b6a4)"></div>
  <h3 class="hl">BOOK KEEPING SERVICES</h3>
  <p>It is a long established fact that a reader will be<br>distracted by the readable content of a page when<br>looking at its layout. The point of using Lorem</p>
</article>
<article class="feature abs" style="left:447px">
  <div class="feature-img" role="img" aria-label="Photo of a businessman touching floating dollar symbols" style="background:linear-gradient(150deg,#9fb6cf,#4d6f96 55%,#2f4766)"></div>
  <h3>FINANCIAL ADVICE</h3>
  <p>It is a long established fact that a reader will be<br>distracted by the readable content of a page when<br>looking at its layout. The point of using Lorem</p>
</article>
<article class="feature abs" style="left:794px">
  <div class="feature-img" role="img" aria-label="Photo of colleagues meeting around a laptop in an office" style="background:linear-gradient(150deg,#c9ced2,#8a8f92 50%,#4e4f4f)"></div>
  <h3>ACCOUNTING ADVICE</h3>
  <p>It is a long established fact that a reader will be<br>distracted by the readable content of a page when<br>looking at its layout. The point of using Lorem</p>
</article>
<div class="feature-line abs" style="left:99px"></div>
<div class="feature-line abs" style="left:447px"></div>
<div class="feature-line abs" style="left:794px"></div>

<section class="services abs"></section>
<h2 class="services-title heading abs">Our Services</h2>

<div class="service abs" style="left:99px;top:1336px">
  <svg width="30" height="30" viewBox="0 0 30 30"><rect x="3" y="5" width="24" height="22" rx="5" fill="#444"/><circle cx="11" cy="14" r="2" fill="#fff"/><circle cx="19" cy="14" r="2" fill="#fff"/><path d="M11 20h8" stroke="#fff" stroke-width="2"/></svg>
  <h4>Our Story</h4>
  <p>Brightfold is a California-based company focused on providing managed and optimized hosting services to small, medium-size ...</p>
</div>
<div class="service abs" style="left:447px;top:1336px">
  <svg width="30" height="30" viewBox="0 0 30 30"><path d="M3 11L15 3l12 8z" fill="#444"/><rect x="6" y="13" width="3" height="11" fill="#444"/><rect x="13.5" y="13" width="3" height="11" fill="#444"/><rect x="21" y="13" width="3" height="11" fill="#444"/><rect x="3" y="25" width="24" height="3" fill="#444"/></svg>
  <h4>Our Story</h4>
  <p>Brightfold is a California-based company focused on providing managed and optimized hosting services to small, medium-size ...</p>
</div>
<div class="service abs" style="left:794px;top:1336px">
  <svg width="30" height="30" viewBox="0 0 30 30"><circle cx="15" cy="17" r="11" fill="none" stroke="#444" stroke-width="2.5"/><path d="M15 17V10M12 3h6" stroke="#444" stroke-width="2.5"/></svg>
  <h4>Our Story</h4>
  <p>Brightfold is a California-based company focused on providing managed and optimized hosting services to small, medium-size ...</p>
</div>
<div class="service abs" style="left:99px;top:1466px">
  <svg width="30" height="30" viewBox="0 0 30 30"><path d="M4 8a4 4 0 014-4h12a4 4 0 014 4v6a4 4 0 01-4 4h-8l-6 5v-5a4 4 0 01-2-3z" fill="none" stroke="#444" stroke-width="2"/><path d="M25 13h1a3 3 0 013 3v5a3 3 0 01-2 3v4l-5-4h-6" fill="none" stroke="#444" stroke-width="2"/></svg>
  <h4>Data Center</h4>
  <p>Brightfold is a California-based company focused on providing managed and optimized hosting services to small, medium-size ...</p>
</div>
<div class="service abs" style="left:447px;top:1466px">
  <svg width="30" height="30" viewBox="0 0 30 30"><circle cx="9" cy="9" r="6" fill="none" stroke="#444" stroke-width="2"/><rect x="14" y="15" width="13" height="3" fill="#444"/><rect x="14" y="20" width="13" height="3" fill="#444"/><rect x="14" y="25" width="13" height="3" fill="#444"/></svg>
  <h4>Data Center</h4>
  <p>Brightfold is a California-based company focused on providing managed and optimized hosting services to small, medium-size ...</p>
</div>
<div class="service abs" style="left:794px;top:1466px">
  <svg width="30" height="30" viewBox="0 0 30 30"><rect x="3" y="5" width="3" height="22" fill="#444"/><rect x="9" y="10" width="3" height="17" fill="#444"/><rect x="15" y="14" width="3" height="13" fill="#444"/><rect x="21" y="18" width="3" height="9" fill="#444"/><path d="M5 6l22 12" stroke="#444" stroke-width="2"/></svg>
  <h4>Data Center</h4>
  <p>Brightfold is a California-based company focused on providing managed and optimized hosting services to small, medium-size ...</p>
</div>

<section class="stats abs"></section>
<h2 class="stats-title heading abs">We help you in book keeping &amp; accounting</h2>
<p class="stats-text abs">There are many variations of passages of Lorem Ipsum available, but the majority have suffered alteration in some form, by injected humour, or randomised words which don't look even slightly believable. If you are going to use a passage</p>

<div class="stat abs" style="left:167px">
  <svg width="160" height="160" viewBox="0 0 160 160"><circle cx="80" cy="80" r="76" fill="none" stroke="rgba(255,255,255,.45)" stroke-width="3"/><path d="M80 4A76 76 0 0 1 153 60" fill="none" stroke="var(--sky)" stroke-width="5"/></svg>
  <b>248</b><span>Year of Experience</span>
</div>
<div class="stat abs" style="left:404px">
  <svg width="160" height="160" viewBox="0 0 160 160"><circle cx="80" cy="80" r="76" fill="none" stroke="rgba(255,255,255,.45)" stroke-width="3"/><path d="M80 4A76 76 0 0 1 156 80" fill="none" stroke="var(--sky)" stroke-width="5"/></svg>
  <b>1950</b><span>Happy Customers</span>
</div>
<div class="stat abs" style="left:644px">
  <svg width="160" height="160" viewBox="0 0 160 160"><circle cx="80" cy="80" r="76" fill="none" stroke="rgba(255,255,255,.45)" stroke-width="3"/><path d="M80 4A76 76 0 0 1 140 126" fill="none" stroke="var(--sky)" stroke-width="5"/></svg>
  <b>2686</b><span>Satisfaction</span>
</div>
<div class="stat abs" style="left:881px">
  <svg width="160" height="160" viewBox="0 0 160 160"><circle cx="80" cy="80" r="76" fill="none" stroke="rgba(255,255,255,.45)" stroke-width="3"/><path d="M80 4A76 76 0 1 1 22 129" fill="none" stroke="var(--sky)" stroke-width="5"/></svg>
  <b>3698</b><span>Projects</span>
</div>

<h2 class="testi-title heading abs">Our Testimonial</h2>

<blockquote class="quote-card abs" style="left:99px">" Venture partners may earn the right to be a Part-<br>ner according to the time period they spent and the<br>evaluation process. Venture partners may earn the<br>right to be a Partner according to the time "</blockquote>
<blockquote class="quote-card abs" style="left:440px">" Venture partners may earn the right to be a Part-<br>ner according to the time period they spent and the<br>evaluation process. Venture partners may earn the<br>right to be a Partner according to the time "</blockquote>
<blockquote class="quote-card abs" style="left:779px">" Venture partners may earn the right to be a Part-<br>ner according to the time period they spent and the<br>evaluation process. Venture partners may earn the<br>right to be a Partner according to the time "</blockquote>

<svg class="quote-pin abs" style="left:231px" viewBox="0 0 58 58"><circle cx="29" cy="29" r="28" fill="var(--teal-soft)"/><circle cx="29" cy="29" r="22" fill="var(--teal)"/><path d="M19 24h8v8l-4 6h-3l3-6h-4zM31 24h8v8l-4 6h-3l3-6h-4z" fill="#fff"/></svg>
<svg class="quote-pin abs" style="left:572px" viewBox="0 0 58 58"><circle cx="29" cy="29" r="28" fill="var(--teal-soft)"/><circle cx="29" cy="29" r="22" fill="var(--teal)"/><path d="M19 24h8v8l-4 6h-3l3-6h-4zM31 24h8v8l-4 6h-3l3-6h-4z" fill="#fff"/></svg>
<svg class="quote-pin abs" style="left:911px" viewBox="0 0 58 58"><circle cx="29" cy="29" r="28" fill="var(--teal-soft)"/><circle cx="29" cy="29" r="22" fill="var(--teal)"/><path d="M19 24h8v8l-4 6h-3l3-6h-4zM31 24h8v8l-4 6h-3l3-6h-4z" fill="#fff"/></svg>

<div class="author abs" style="left:99px"><div class="avatar" role="img" aria-label="Client portrait photo"></div></div>
<div class="author-name abs" style="left:181px">Deniz Aldemir</div>
<div class="author-role abs" style="left:181px">Startup Harbor</div>
<div class="author abs" style="left:440px"><div class="avatar" role="img" aria-label="Client portrait photo"></div></div>
<div class="author-name abs" style="left:522px">Deniz Aldemir</div>
<div class="author-role abs" style="left:522px">Startup Harbor</div>
<div class="author abs" style="left:779px"><div class="avatar" role="img" aria-label="Client portrait photo"></div></div>
<div class="author-name abs" style="left:861px">Deniz Aldemir</div>
<div class="author-role abs" style="left:861px">Startup Harbor</div>

<footer>
  <section class="newsletter abs"></section>
  <h2 class="news-title heading abs">NEWSLETTER</h2>
  <p class="news-sub abs">We promise only send the good things</p>
  <div class="news-input abs">Enter Your Mail Id</div>
  <div class="news-btn abs"><svg width="70" height="43" viewBox="0 0 70 43"><path d="M43 14L27 21l7 2 2 7z" fill="#fff"/></svg></div>

  <div class="foot-col abs" style="left:97px"><h5>ABOUT US</h5><a>Home</a><a>Service</a><a>Compare</a><a>Experience</a></div>
  <div class="foot-col abs" style="left:315px"><h5>INFORMATION</h5><a>Testimonials</a><a>Resources</a><a>Contact Us</a></div>
  <div class="foot-col abs" style="left:538px"><h5>CUSTOMER</h5><a>Privacy policy</a><a>Terms &amp; Conditions</a><a>Sitemap</a></div>
  <div class="foot-col abs" style="left:763px"><h5>MAIN MENU</h5><a>About Us</a><a>Services</a><a>Experience</a><a>Contact Us</a></div>
  <div class="foot-col abs" style="left:988px"><h5>OUR PROJECTS</h5><a>Neque porro</a><a>Quisquam lat</a><a>Quia dolor sit amet</a><a>The standard Lorem</a></div>

  <div class="bottom-bar abs">Copyright©2016 Company Name . All rights Reserved</div>
</footer>

</body>
</html>
```